Business Card Design Project

Business Card
We are rebranding with a new logo
Industry/Entity Type
Business
Contact Information for Business Card
Dennis Marlow +61 427581962 dennis@qovo.com.au P.O. Box 872 Kelvindale QLD 4309
Requirements
Must have
- Logo

```html
<!DOCTYPE html>
<html lang="en">
<head>
<meta charset="utf-8">
<title>Qovo International – Business Card</title>
<link rel="stylesheet" href="https://fonts.googleapis.com/css2?family=Jost:wght@400;500;600&display=swap">
<style>
  :root {
    --paper: #ffffff;
    --sea-blue: #0198d3;
    --brand-blue: #0b6fa8;
    --orange: #f47a20;
    --orange-deep: #d2682a;
    --ink-light: #ffffff;
    --edge: #5a5a5a;
  }
  html, body {
    margin: 0;
    padding: 0;
    overflow: hidden;
    background: var(--paper);
  }
  .card {
    position: relative;
    width: 1200px;
    height: 677px;
    background: var(--paper);
    box-sizing: border-box;
    border: 1px solid var(--edge);
    overflow: hidden;
    font-family: "Jost", "Futura", sans-serif;
  }
  .card__wave {
    position: absolute;
    inset: 0;
    width: 100%;
    height: 100%;
  }
  .wave-rim { fill: var(--orange-deep); }
  .wave-band { fill: var(--orange); }
  .wave-sea { fill: var(--sea-blue); }
  .brand {
    position: absolute;
    left: 64px;
    top: 150px;
    margin: 0;
    font-size: 50px;
    font-weight: 500;
    letter-spacing: 1px;
    color: var(--brand-blue);
    line-height: 1;
  }
  .contact {
    position: absolute;
    right: 85px;
    top: 408px;
    margin: 0;
    text-align: right;
    color: var(--ink-light);
    font-size: 35px;
    line-height: 52px;
    font-weight: 400;
    font-style: normal;
  }
  .contact__name {
    font-weight: 600;
    font-size: 35px;
  }
</style>
</head>
<body>
  <div class="card">
    <svg class="card__wave" viewBox="0 0 1200 677" aria-hidden="true">
      <path class="wave-rim" d="M0,330 C120,395 260,420 420,390 C600,352 720,222 900,220 C1020,218 1120,240 1200,255 L1200,677 L0,677 Z"/>
      <path class="wave-band" d="M0,342 C120,408 260,430 420,400 C600,362 720,236 900,234 C1020,232 1120,254 1200,269 L1200,677 L0,677 Z"/>
      <path class="wave-rim" d="M0,360 C120,424 260,446 420,416 C600,380 720,262 900,262 C1020,262 1120,282 1200,297 L1200,677 L0,677 Z"/>
      <path class="wave-sea" d="M0,368 C120,432 260,452 420,422 C600,388 720,272 900,272 C1020,272 1120,292 1200,307 L1200,677 L0,677 Z"/>
    </svg>

    <p class="brand">Qovo International</p>

    <address class="contact">
      <div class="contact__name">Dennis Marlow</div>
      <div class="contact__phone">+61 427581962</div>
      <div class="contact__email">dennis@qovo.com.au</div>
      <div class="contact__post">P.O. Box 872 Kelvindale QLD 4309</div>
    </address>
  </div>
</body>
</html>
```